"Pillowtide Chews" is the brand name for CBN infused Gummies for a restful sleep

Need a label for the glass jar and a round label for the lid. The gummy shapes are crescent white mons and blue stars or gummy sheep

You can use an 6 or 8 oz clear jar. Your illustration program should have this mock up.

Font styles to use
Sans Serif

```html
<!DOCTYPE html>
<html lang="en">
<head>
<meta charset="utf-8">
<title>Pillowtide Chews – Jar Label Options</title>
<link rel="stylesheet" href="https://fonts.googleapis.com/css2?family=Poppins:wght@600;700&family=Montserrat:wght@400;500&family=Barlow+Semi+Condensed:wght@500;600;700&display=swap">
<style>
  :root {
    --stage: #4a4a4a;
    --stage-low: #333333;
    --navy: #17245a;
    --navy-glow: #2c4785;
    --leaf: #2f4b8c;
    --moon: #fde06a;
    --white: #ffffff;
    --ink: #1a2a5e;
    --badge: #000000;
  }
  * { box-sizing: border-box; margin: 0; padding: 0; }
  html, body { width: 1200px; height: 809px; overflow: hidden; }
  body {
    position: relative;
    background: linear-gradient(to bottom, var(--stage) 0, var(--stage) 62%, var(--stage-low) 62%, var(--stage-low) 100%);
    font-family: "Montserrat", sans-serif;
    color: var(--white);
  }
  .option-badge {
    position: absolute;
    width: 106px; height: 106px;
    border-radius: 50%;
    background: var(--badge);
    border: 3px solid var(--white);
    color: var(--white);
    font: 700 72px/100px "Poppins", sans-serif;
    text-align: center;
  }
  .option-badge--one { left: 133px; top: 47px; }
  .option-badge--two { left: 598px; top: 47px; }

  .night-decor {
    position: absolute; left: 966px; top: 28px; width: 181px; height: 111px;
    background: radial-gradient(ellipse at 55% 50%, #f7b10a 0 28%, rgba(255,255,255,0.85) 29% 45%, transparent 65%);
  }

  .jar-label {
    position: absolute; top: 240px;
    width: 393px; height: 372px;
    background: var(--navy);
    overflow: hidden;
  }
  .jar-label--classic { left: 192px; }
  .jar-label--leaf { left: 640px; }

  .label-halo {
    position: absolute; left: 21px; top: -108px;
    width: 354px; height: 354px; border-radius: 50%;
    background: var(--navy-glow);
  }
  .leaf-art {
    position: absolute;
    background: radial-gradient(ellipse at 50% 55%, var(--leaf) 0 45%, rgba(47,75,140,0.4) 65%, transparent 72%);
  }
  .jar-label--classic .leaf-art { left: -40px; top: 215px; width: 190px; height: 170px; }
  .jar-label--leaf .leaf-art { left: 12px; top: 8px; width: 372px; height: 351px; }

  .night-art {
    position: absolute; left: 140px; top: 26px; width: 137px; height: 85px;
    background: radial-gradient(ellipse at 55% 50%, var(--moon) 0 30%, rgba(255,255,255,0.9) 31% 42%, transparent 62%);
  }

  .brand-name {
    position: absolute; left: 0; width: 100%;
    font-family: "Poppins", sans-serif; font-weight: 700;
    text-align: center; line-height: 1;
  }
  .jar-label--classic .brand-name { top: 128px; color: var(--moon); font-size: 40px; }
  .jar-label--leaf .brand-name { top: 150px; color: var(--white); font-size: 42px; }
  .brand-name span { display: block; }

  .tagline {
    position: absolute; font-size: 18px; font-weight: 400; letter-spacing: 0.3px; white-space: nowrap;
  }
  .jar-label--classic .tagline { left: 0; width: 100%; text-align: center; top: 255px; }
  .jar-label--leaf .tagline--infusion { left: 0; width: 100%; text-align: center; top: 263px; }
  .jar-label--leaf .tagline--sleep { left: 27px; top: 334px; }

  .infusion-note { position: absolute; right: 24px; top: 290px; font-size: 18px; }

  .nutrition-row {
    position: absolute; left: 235px; top: 317px; display: flex; gap: 3px;
  }
  .nutrition-cell {
    width: 32px; height: 35px; background: var(--white); color: var(--ink);
    border-radius: 16px 16px 0 0; text-align: center;
    font-family: "Barlow Semi Condensed", sans-serif;
    display: flex; flex-direction: column; justify-content: flex-end;
  }
  .nutrition-cell b { font-size: 11px; font-weight: 700; line-height: 1; padding-bottom: 3px; }
  .nutrition-cell small {
    background: var(--navy-glow); color: var(--white); font-size: 5px; font-weight: 600;
    line-height: 10px; height: 10px;
  }

  .dose-block {
    position: absolute; top: 314px;
    font-family: "Barlow Semi Condensed", sans-serif; font-weight: 600; line-height: 1;
  }
  .jar-label--classic .dose-block { left: 24px; }
  .jar-label--leaf .dose-block { right: 29px; text-align: right; }
  .dose-block .big { font-size: 19px; font-weight: 700; }
  .dose-block .mid { font-size: 12px; }
  .dose-block p + p { margin-top: 4px; }
</style>
</head>
<body>
  <div class="option-badge option-badge--one">1</div>
  <div class="option-badge option-badge--two">2</div>
  <div class="night-decor" role="img" aria-label="Crescent moon with clouds and stars"></div>

  <section class="jar-label jar-label--classic">
    <div class="label-halo"></div>
    <div class="leaf-art" role="img" aria-label="Faint botanical leaf decoration"></div>
    <div class="night-art" role="img" aria-label="Crescent moon with clouds and stars"></div>
    <h1 class="brand-name"><span>Pillowtide</span><span>Chews</span></h1>
    <p class="tagline">RESTFUL SLEEP</p>
    <p class="infusion-note">CBN infused</p>
    <div class="nutrition-row">
      <div class="nutrition-cell"><b>280</b><small>CALORIES</small></div>
      <div class="nutrition-cell"><b>10 g</b><small>FAT/LIPIDES</small></div>
      <div class="nutrition-cell"><b>20 mg</b><small>SODIUM</small></div>
      <div class="nutrition-cell"><b>24 g</b><small>SUGARS</small></div>
    </div>
    <div class="dose-block">
      <p><span class="big">30</span><span class="mid">mg CBN</span></p>
      <p><span class="mid">NET WT. </span><span class="big">150g</span></p>
    </div>
  </section>

  <section class="jar-label jar-label--leaf">
    <div class="leaf-art" role="img" aria-label="Large botanical leaf decoration"></div>
    <div class="night-art" role="img" aria-label="Crescent moon with clouds and stars"></div>
    <h1 class="brand-name"><span>Pillowtide</span><span>Chews</span></h1>
    <p class="tagline tagline--infusion">CANNABIS-INFUSED</p>
    <p class="tagline tagline--sleep">RESTFUL SLEEP</p>
    <div class="dose-block">
      <p><span class="mid">CBN </span><span class="big">30</span><span class="mid">mg</span></p>
      <p><span class="mid">NET WT. </span><span class="big">150g</span></p>
    </div>
  </section>
</body>
</html>
```